5 Email Newsletter Templates Needed

We need 5 email templates for our email marketing campaign. We are an Insurance Agency in Los Angeles called KDP-Silverbrook Insurance Services. We use Mailvane Hub as our email marketing platform. The templates need to be simple, a nice header, not to busy and you will need to use our color palette. The first email template we need is for our current clients / prospects. The content we will put in this email will be insurance tips and information, short and simple about 2 small paragraphs. The next 3 templates all need to be the same but different colors. One red, one yellow and one green. These will be alerts from kdp-silverbrook. An example a major earthquake hits we will send a red alert. A legislative change on healthcare and we send a yellow alert. We buy another location and we send a green alert. The last email is for our COINs (Centers of Influence, the people who refer business to us). I uploaded an email from one of our business consultants to give an idea of the size and sophistication we are looking for. I also uploaded our corporate brochure and color palette so you can learn more about our firm.

Target Market(s)

Our target markets are commercial business 1mm plus in revenue, 500 employees, high net worth individuals. Our COINs are CPAs, CFOs, Business Managers

Requirements
Nice to have
• HTML Code is desired. You can also provide just an image file for the header and our email marketing program will do the coding for us.
Should not have
• No cartoon looking graphics. Do not use old-style fonts like Times New Roman.

```html
<!DOCTYPE html>
<html lang="en">
<head>
<meta charset="utf-8">
<title>Tip Number 28 – It's Getting Cold Outside</title>
<link rel="stylesheet" href="https://fonts.googleapis.com/css2?family=Arimo:wght@400;700&display=swap">
<style>
  :root {
    --page-bg: #cfd0cb;
    --card-bg: #ffffff;
    --header-top: #ffffff;
    --header-bottom: #e4e5e3;
    --brand-green: #0a6b5a;
    --ribbon-green: #117a67;
    --headline-blue: #12648a;
    --lead-grey: #9b958a;
    --body-ink: #262626;
    --fine-grey: #9d9d9d;
    --muted-label: #8a8a8a;
    --social-blue: #3b5a98;
    --social-sky: #5fb6d9;
    --footer-ink: #ffffff;
  }
  * { box-sizing: border-box; margin: 0; padding: 0; }
  html, body {
    width: 966px; height: 1200px; overflow: hidden;
    background: var(--page-bg);
    font-family: "Arimo", Arial, sans-serif;
  }
  .canvas { position: relative; width: 966px; height: 1200px; }

  .online-link {
    position: absolute; top: 95px; left: 0; width: 966px;
    text-align: center; font-size: 14px; color: var(--footer-ink);
    text-decoration: underline;
  }

  .newsletter {
    position: absolute; left: 63px; top: 138px; width: 826px; height: 911px;
    background: var(--card-bg);
    box-shadow: 0 4px 9px rgba(0,0,0,0.45);
  }
  .masthead {
    position: absolute; left: 0; top: 0; width: 826px; height: 62px;
    background: linear-gradient(var(--header-top), var(--header-bottom));
  }
  .brand-name {
    position: absolute; left: 37px; top: 31px;
    font-size: 21px; font-weight: 400; letter-spacing: 1px;
    color: var(--brand-green);
  }
  .masthead-band {
    position: absolute; left: 0; top: 62px; width: 826px; height: 14px;
    background: var(--brand-green);
  }

  .tip-ribbon { position: absolute; left: 0; top: 124px; width: 157px; height: 124px; }
  .tip-ribbon svg { position: absolute; inset: 0; }
  .tip-label {
    position: absolute; left: 0; top: 14px; width: 140px; text-align: center;
    font-size: 18px; color: #fff;
  }
  .tip-number {
    position: absolute; left: 0; top: 38px; width: 140px; text-align: center;
    font-size: 66px; line-height: 1; color: #fff; letter-spacing: -2px;
  }

  .follow {
    position: absolute; left: 28px; top: 266px; width: 118px; text-align: center;
  }
  .follow-label { font-size: 14px; color: var(--muted-label); }
  .social-row { display: flex; justify-content: center; gap: 7px; margin-top: 10px; }
  .social-square { width: 21px; height: 21px; border-radius: 3px; }
  .social-square.one { background: var(--social-blue); }
  .social-square.two { background: var(--social-sky); }

  .article { position: absolute; left: 203px; top: 0; width: 540px; }
  .headline {
    position: absolute; top: 157px; left: 0; width: 560px;
    font-size: 42px; font-weight: 400; color: var(--headline-blue); white-space: nowrap;
  }
  .lead {
    position: absolute; top: 233px; left: 0; width: 525px;
    font-size: 21.5px; line-height: 28px; color: var(--lead-grey);
  }
  .body-copy {
    position: absolute; left: 0; width: 540px;
    font-size: 17.5px; line-height: 27.6px; color: var(--body-ink);
  }
  .body-copy.first { top: 395px; }
  .body-copy.second { top: 561px; }
  .fine-print {
    position: absolute; top: 726px; left: 0; width: 530px;
    font-size: 13.5px; line-height: 20.7px; color: var(--fine-grey);
  }

  .footer-address {
    position: absolute; left: 86px; top: 1071px;
    font-size: 14.5px; line-height: 20.7px; color: var(--footer-ink);
  }
  .unsubscribe {
    position: absolute; right: 106px; top: 1073px;
    font-size: 14.5px; color: var(--footer-ink); text-decoration: underline;
  }
</style>
</head>
<body>
<div class="canvas">
  <a class="online-link">View the online version</a>

  <main class="newsletter">
    <header class="masthead">
      <div class="brand-name">KDP-SILVERBROOK INSURANCE SERVICES</div>
    </header>
    <div class="masthead-band"></div>

    <div class="tip-ribbon">
      <svg width="157" height="124" viewBox="0 0 157 124" aria-hidden="true">
        <polygon points="0,0 137,0 157,62 137,124 0,124" fill="var(--ribbon-green)"/>
      </svg>
      <div class="tip-label">Tip Number</div>
      <div class="tip-number">28</div>
    </div>

    <aside class="follow">
      <div class="follow-label">Follow Us</div>
      <div class="social-row">
        <span class="social-square one"></span>
        <span class="social-square two"></span>
      </div>
    </aside>

    <article class="article">
      <h1 class="headline">It's Getting Cold Outside.</h1>
      <p class="lead">Lorem ipsum dolor sit amet, consectetuer adipiscing elit, sed diam nonummy nibh euismod tincidunt ut laoreet dolore magna aliquam erat volutpat. Ut wisi enim ad minim veniam.</p>
      <p class="body-copy first">Lorem ipsum dolor sit amet, consectetuer adipiscing elit, sed diam nonummy nibh euismod tincidunt ut laoreet dolore magna aliquam erat volutpat. Ut wisi enim ad minim veniam, quis nostrud exerci tation ullamcorper suscipit lobortis nisl ut aliquip ex ea commodo consequat.</p>
      <p class="body-copy second">Duis autem vel eum iriure dolor in hendrerit in vulputate velit esse molestie consequat, vel illum dolore eu feugiat nulla facilisis at vero eros et accumsan et iusto odio dignissim qui blandit praesent luptatum zzril delenit augue duis dolore te feugait nulla facilisi.</p>
      <p class="fine-print">Lorem ipsum dolor sit amet, consectetuer adipiscing elit, sed diam nonummy nibh euismod tincidunt ut laoreet dolore magna aliquam erat volutpat. Ut wisi enim ad minim veniam, quis nostrud exerci tation ullamcorper suscipit lobortis nisl ut aliquip ex ea.</p>
    </article>
  </main>

  <footer>
    <div class="footer-address">
      Northgate Continuity Partners<br>
      4820 Alder Park Dr - Suite 210<br>
      Riverton, NC 28990<br>
      555.014.2280
    </div>
    <a class="unsubscribe">Unsubscribe</a>
  </footer>
</div>
</body>
</html>
```